Japanese Rice Food Package Label

- We are launching Japanese food products to the outdoor community.
- Made in Japan
- We will have multiple flavors of rice but want to keep the package label almost the same and only replace the flavor text (e.g., Mixed Rice, Curry Rice, etc)
- We like simple designs inspired by Japan.
- Label size: 105 mm x148 mm
- Our brand: YOBEN https://yoben.co/
- Video message: https://www.vidqo.com/share/3f51b07a9e2c4d6891a0c7e5b2d94f18

```html
<!DOCTYPE html>
<html lang="en">
<head>
<meta charset="utf-8">
<title>YOBEN Mixed Rice – Package Label</title>
<link rel="stylesheet" href="https://fonts.googleapis.com/css2?family=Montserrat:wght@800&family=Kanit:wght@400&family=Ubuntu:wght@400&family=Open+Sans:wght@400&family=Oswald:wght@500&display=swap">
<style>
  :root {
    --page-bg: #ececec;
    --label-bg: #ffffff;
    --ink: #0c0c0c;
    --flavor-yellow: #f2c500;
    --rule-gold: #ecd06a;
    --badge-red: #e31e24;
    --art-beige: #c9b89c;
    --art-light: #f4efe6;
  }
  * { margin: 0; padding: 0; box-sizing: border-box; }
  html, body {
    width: 1200px; height: 1200px; overflow: hidden;
    background: var(--page-bg);
  }
  .label {
    position: absolute; left: 114px; top: 345px;
    width: 967px; height: 686px;
    background: var(--label-bg);
    overflow: hidden;
  }
  .brand {
    position: absolute; left: 72px; top: 28px;
    font-family: "Montserrat", sans-serif; font-weight: 800;
    font-size: 124px; line-height: 1; letter-spacing: -3px;
    color: var(--ink); white-space: nowrap; z-index: 2;
  }
  .brand sup { font-size: 26px; vertical-align: top; position: relative; top: 18px; letter-spacing: 0; margin-left: 4px; }
  .origin-columns {
    position: absolute; left: 79px; top: 201px; width: 42px; height: 177px;
    background: linear-gradient(90deg, #2a2a2a 0 34%, transparent 34% 66%, #2a2a2a 66% 100%);
    opacity: .18;
  }
  .flavor {
    position: absolute; left: 150px;
    font-family: "Kanit", sans-serif; font-weight: 400;
    color: var(--flavor-yellow); font-size: 94px; line-height: 1;
    white-space: nowrap;
  }
  .flavor--top { top: 183px; }
  .flavor--bottom { top: 283px; }
  .dotted {
    position: absolute; left: 152px; height: 0;
    border-top: 3px dotted var(--ink);
  }
  .dotted--top { top: 286px; width: 231px; }
  .dotted--bottom { top: 376px; width: 181px; }
  .rule {
    position: absolute; left: 82px; width: 256px; height: 1px;
    background: var(--rule-gold);
  }
  .rule--1 { top: 421px; } .rule--2 { top: 484px; } .rule--3 { top: 568px; }
  .product-type {
    position: absolute; left: 80px; top: 427px;
    font-family: "Ubuntu", sans-serif; font-size: 47px; line-height: 1.1;
    color: var(--ink); white-space: nowrap;
  }
  .prep {
    position: absolute; top: 500px; width: 130px; text-align: center;
    font-family: "Open Sans", sans-serif; font-size: 16px; line-height: 27px;
    color: var(--ink); white-space: nowrap;
  }
  .prep--water { left: 62px; } .prep--time { left: 221px; }
  .vdivider { position: absolute; width: 1px; background: var(--rule-gold); }
  .vdivider--prep { left: 210px; top: 495px; height: 64px; }
  .vdivider--b1 { left: 188px; top: 583px; height: 66px; }
  .vdivider--b2 { left: 274px; top: 583px; height: 66px; }
  .badge { position: absolute; top: 581px; width: 100px; text-align: center; }
  .badge svg { display: block; margin: 0 auto; }
  .badge span {
    display: block; margin-top: 4px;
    font-family: "Oswald", sans-serif; font-weight: 500; font-size: 12px;
    color: var(--ink); white-space: nowrap;
  }
  .badge--flavors { left: 80px; } .badge--natural { left: 181px; } .badge--gmo { left: 262px; }
  .artwork {
    position: absolute; left: 535px; top: 0; width: 432px; height: 686px;
    background: radial-gradient(circle at 50% 62%, var(--art-beige) 0 26%, var(--art-light) 52%, #ffffff 82%);
    clip-path: polygon(130px 0, 100% 0, 100% 100%, 0 100%, 0 240px, 130px 200px);
  }
</style>
</head>
<body>
  <main class="label">
    <h1 class="brand">YOBEN<sup>®</sup></h1>

    <div class="origin-columns" role="img" aria-label="Decorative vertical Japanese-style lettering"></div>

    <h2 class="flavor flavor--top">MIXED</h2>
    <div class="dotted dotted--top"></div>
    <h2 class="flavor flavor--bottom">RICE</h2>
    <div class="dotted dotted--bottom"></div>

    <div class="rule rule--1"></div>
    <p class="product-type">Instant Rice</p>
    <div class="rule rule--2"></div>

    <p class="prep prep--water">JUST ADD<br>HOT WATER</p>
    <div class="vdivider vdivider--prep"></div>
    <p class="prep prep--time">READY<br>IN 5 MINS</p>

    <div class="rule rule--3"></div>

    <div class="badge badge--flavors">
      <svg width="52" height="52" viewBox="0 0 60 60" aria-hidden="true">
        <circle cx="30" cy="30" r="29" fill="var(--badge-red)"/>
        <circle cx="30" cy="30" r="22" fill="none" stroke="#fff" stroke-width="3"/>
        <line x1="15" y1="15" x2="45" y2="45" stroke="#fff" stroke-width="3"/>
      </svg>
      <span>No Artificial Flavors</span>
    </div>
    <div class="vdivider vdivider--b1"></div>
    <div class="badge badge--natural">
      <svg width="52" height="52" viewBox="0 0 60 60" aria-hidden="true">
        <circle cx="30" cy="30" r="29" fill="var(--badge-red)"/>
        <circle cx="30" cy="30" r="22" fill="none" stroke="#fff" stroke-width="3"/>
        <path d="M20 38 C20 26 28 20 40 20 C40 32 32 38 20 38 Z" fill="#fff"/>
      </svg>
      <span>100% Natural</span>
    </div>
    <div class="vdivider vdivider--b2"></div>
    <div class="badge badge--gmo">
      <svg width="52" height="52" viewBox="0 0 60 60" aria-hidden="true">
        <circle cx="30" cy="30" r="29" fill="var(--badge-red)"/>
        <circle cx="30" cy="30" r="22" fill="none" stroke="#fff" stroke-width="3"/>
        <line x1="15" y1="15" x2="45" y2="45" stroke="#fff" stroke-width="3"/>
      </svg>
      <span>Non GMO</span>
    </div>

    <div class="artwork" role="img" aria-label="Illustration of a rice bowl with chopsticks before a red sun, framed by line-drawn flowers and waves"></div>
  </main>
</body>
</html>
```